Member Dashboard needs a facelift

Our company is in the consumer credit industry. We offer a service, and once a person signs up for that service, they become a "Member". As a member, they can sign into our "Member Dashboard". What we are looking for is a facelift to our current "Member Dashboard" pages.

We are looking for a cleaner, more modern design that incorporates the same functionality of the current pages (tabs and charts). The graphics elements, buttons and top navigation menu need updating as well.

We are looking for only the page design "look and Feel" and some new great ideas graphicly. Not looking for an entire site.

Please note that the grey background shown in the screen shots is full browser width.

Thank you.
Updates

Thank you everyone for your designs.  Please make sure all designs are in by the end of day.  We will be selecting the 1st and 2nd design tomorrow AM.

 

Thank you for your partisapation.

 

Target Market(s)

Adults over the age of 18 who pay rent in housing.

Industry/Entity Type

Industry

Requirements
Must have
• We are looking for a professional modern look that keeps with the current structure of the current member dashboard. The pages are 1152px wide.

```html
<!DOCTYPE html>
<html lang="en">
<head>
<meta charset="utf-8">
<title>Member Dashboard</title>
<link href="https://fonts.googleapis.com/css2?family=Arimo:wght@400;700&display=swap" rel="stylesheet">
<style>
:root{
  --page-bg:#f2f2f2;
  --card:#ffffff;
  --card-border:#e3e3e3;
  --brand:#1a8fc1;
  --brand-dark:#0f7aa8;
  --brand-light:#5cc6ea;
  --heading:#2a9fd0;
  --text:#333333;
  --muted:#555555;
  --gauge-red:#c6283a;
  --gauge-orange:#ee8d4a;
  --gauge-green:#3ea94a;
  --pie-blue:#0a3ffb;
  --pie-green:#35cc0f;
  --pie-orange:#fb8a1e;
  --pie-red:#d30b0b;
  --pie-yellow:#f4e400;
}
*{box-sizing:border-box;margin:0;padding:0}
html,body{width:933px;height:1200px;overflow:hidden}
body{background:linear-gradient(#fafafa,#ececec 560px,#f7f7f7);font-family:"Arimo",Arial,sans-serif;color:var(--text);position:relative}
.box{position:absolute;background:var(--card);border:1px solid var(--card-border);border-radius:6px;box-shadow:0 1px 4px rgba(0,0,0,.08)}
.header{left:47px;top:0;width:839px;height:72px;border-top:none;border-radius:0 0 6px 6px}
.logo{position:absolute;left:17px;top:22px;font-size:23px;font-weight:700;color:var(--brand)}
.top-links{position:absolute;right:18px;top:32px;font-size:10px;font-weight:700;display:flex;gap:14px;align-items:center}
.top-links span{display:flex;align-items:center;gap:4px}
.nav{position:absolute;left:47px;top:78px;width:839px;height:33px;border-radius:5px;background:linear-gradient(#7fd7f2,#2cb0dc 50%,#149ccb 51%,#1796c5);display:flex;box-shadow:0 2px 3px rgba(0,0,0,.2)}
.nav a{color:#fff;font-size:10px;font-weight:700;text-transform:uppercase;text-decoration:none;display:flex;align-items:center;justify-content:center;border-right:1px solid rgba(255,255,255,.35);text-shadow:0 1px 1px rgba(0,0,0,.3)}
.nav a:last-child{border-right:none}
.nav a.active{background:linear-gradient(#3cb4da,#0d85b3);border-radius:5px 0 0 5px}
.subtabs{position:absolute;left:95px;top:127px;display:flex;gap:4px}
.subtabs a{height:23px;padding:0;white-space:nowrap;display:flex;align-items:center;justify-content:center;font-size:9px;font-weight:700;color:#fff;background:linear-gradient(#56c2e6,#1a93c2);border-radius:5px 5px 0 0;text-decoration:none}
.subtabs a.current{background:#fff;color:var(--brand);border:1px solid var(--card-border);border-bottom:none}
.landlord{left:47px;top:151px;width:495px;height:388px;padding:15px 14px}
h2{font-size:20px;font-weight:700;color:var(--heading)}
.landlord p{font-size:8.6px;line-height:14px;color:var(--muted);margin-top:6px}
.fields{margin-top:13px;height:198px;background:linear-gradient(#fbfbfb,#f0f0f0);border:1px solid #e2e2e2;border-radius:5px;padding:6px 10px}
.fields div{font-size:8.4px;font-weight:700;height:19px;line-height:19px}
.btn{display:inline-flex;align-items:center;justify-content:center;gap:4px;color:#fff;font-size:8.5px;font-weight:700;background:linear-gradient(#5bc6ea,#1287b7);border-radius:6px;box-shadow:0 1px 2px rgba(0,0,0,.3)}
.edit{margin-top:11px;width:55px;height:22px}
.verify{left:558px;top:151px;width:328px;height:303px;padding:14px 18px}
.verify h2{color:#9e9e9e}
.gauges{display:grid;grid-template-columns:1fr 1fr;column-gap:30px;row-gap:28px;margin-top:8px}
.gauge{text-align:center}
.gauge svg{display:block;margin:0 auto}
.gauge .ends{display:flex;justify-content:space-between;font-size:7.5px;width:118px;margin:0 auto}
.pill{display:inline-block;margin-top:5px;padding:4px 7px;font-size:7.8px;font-weight:700;background:linear-gradient(#fff,#ececec);border:1px solid #d8d8d8;border-radius:8px;white-space:nowrap}
.pill.on{background:linear-gradient(#4fc0e6,#1289b9);color:#fff;border-color:#1289b9}
.notice{left:558px;top:469px;width:328px;height:70px;display:flex;align-items:center;gap:12px;padding:0 14px;font-size:12.5px;line-height:19px;color:#444}
.notice span{width:200px}
.rule{position:absolute;left:47px;width:839px;height:2px;background:#dcdcdc}
.factors-title{position:absolute;left:46px;top:567px;font-size:17px;color:var(--heading)}
.factors-intro{position:absolute;left:49px;top:596px;width:470px;font-size:9.4px;line-height:13px;color:var(--muted)}
.pie{position:absolute;left:46px;top:640px}
.pie-label{position:absolute;font-size:16px;line-height:22px;color:#111}
.legend{left:558px;top:569px;width:328px;height:398px;padding:16px 15px}
.legend h3{display:flex;align-items:center;gap:8px;font-size:16px;font-weight:400;color:var(--heading)}
.legend h3 i{width:18px;height:18px;display:inline-block;border-radius:2px}
.legend p{font-size:9.4px;line-height:14px;color:#444;margin:5px 0 9px}
.card{top:990px;width:114px;height:163px;text-align:center;padding-top:11px}
.card h4{font-size:12px;font-weight:400;color:var(--heading)}
.card .icon{height:60px;display:flex;align-items:center;justify-content:center;margin-top:6px}
.card p{font-size:8.4px;line-height:13px;color:#444;margin-top:4px;height:28px}
.card .btn{width:55px;height:21px;margin-top:9px}
.cta{position:absolute;left:707px;top:988px;width:179px;height:165px;border-radius:6px;background:linear-gradient(#3fb8e2,#1597c7);overflow:hidden;color:#fff;text-align:center}
.cta::before{content:"";position:absolute;left:-40px;top:-130px;width:270px;height:250px;border-radius:50%;background:rgba(255,255,255,.12)}
.cta .big{position:relative;margin-top:14px;font-size:21px;font-weight:700;line-height:27px;text-shadow:0 1px 2px rgba(0,0,0,.25)}
.cta .more{position:absolute;left:24px;bottom:12px;display:flex;align-items:center;gap:12px;font-size:16px;font-weight:700}
.copyright{position:absolute;left:0;width:933px;top:1179px;text-align:center;font-size:8px;color:#333}
</style>
</head>
<body>

<header class="box header">
  <div class="logo">LOGO GOES HERE</div>
  <div class="top-links">
    <span><svg width="12" height="10" viewBox="0 0 12 10"><rect x="0.5" y="1" width="11" height="8" rx="1" fill="#5bbbe0"/><path d="M1 2l5 4 5-4" stroke="#fff" fill="none"/></svg>Contact Support</span>
    <span><svg width="11" height="12" viewBox="0 0 11 12"><rect x="1" y="5" width="9" height="7" rx="1" fill="#5bbbe0"/><path d="M3 5V3a2.5 2.5 0 0 1 5 0" stroke="#5bbbe0" fill="none" stroke-width="1.5"/></svg>Logout</span>
  </div>
</header>

<nav class="nav">
  <a class="active" style="width:168px">Member Home</a>
  <a style="width:203px">Rent Profile</a>
  <a style="width:204px">Credit Summary</a>
  <a style="width:264px">Frequently Asked Questions</a>
</nav>

<div class="subtabs">
  <a style="width:97px">Member Name</a>
  <a style="width:93px">Rental Address</a>
  <a style="width:97px">Member Contact</a>
  <a class="current" style="width:94px">Landlord Contact</a>
</div>

<section class="box landlord">
  <h2>Landlord Verification Center</h2>
  <p>One of the most important aspects of the service is our ability to communicate with your landlord or property manager and interface closely as we gather rent payment data to send on the credit bureau.</p>
  <p style="margin-top:14px">The landlord data we have in our database appears below. Please click on the "edit" button to make changes. Remember, though, that this information is critical to our electronic interface with your landlord/property manager. Changes alert us to a possibility that you have moveda and triggers a verification process that should be avoided unless absolutely necessary.</p>
  <div class="fields">
    <div>Landlord Management :</div>
    <div>Street Address 2 :</div>
    <div>Zip Code :</div>
    <div>Landlord Email :</div>
    <div>Complex / Property Name :</div>
    <div>City :</div>
    <div>Landlord Phone Number :</div>
    <div>Street Address 1 :</div>
    <div>State :</div>
    <div>Landlord Fax Number :</div>
  </div>
  <span class="btn edit"><svg width="9" height="9" viewBox="0 0 9 9"><path d="M1 8l1-3 4-4 2 2-4 4z" fill="#f3c640"/></svg>Edit</span>
</section>

<section class="box verify">
  <h2>Member Verification Center</h2>
  <div class="gauges">
    <div class="gauge">
      <svg width="118" height="62" viewBox="0 0 118 62">
        <path d="M4 58A55 55 0 0 1 31 11L59 58Z" fill="var(--gauge-red)"/>
        <path d="M31 11A55 55 0 0 1 87 11L59 58Z" fill="var(--gauge-orange)"/>
        <path d="M87 11A55 55 0 0 1 114 58L59 58Z" fill="var(--gauge-green)"/>
        <path d="M4 58A55 55 0 0 1 114 58" fill="none" stroke="#333" stroke-width="2"/>
        <line x1="59" y1="58" x2="61" y2="10" stroke="#111" stroke-width="3"/>
        <circle cx="59" cy="58" r="5" fill="#111"/><circle cx="59" cy="58" r="2" fill="#fff"/>
      </svg>
      <div class="ends"><span>Needs Attention</span><span>Verified</span></div>
      <span class="pill">Member Name Verification</span>
    </div>
    <div class="gauge">
      <svg width="118" height="62" viewBox="0 0 118 62">
        <path d="M4 58A55 55 0 0 1 31 11L59 58Z" fill="var(--gauge-red)"/>
        <path d="M31 11A55 55 0 0 1 87 11L59 58Z" fill="var(--gauge-orange)"/>
        <path d="M87 11A55 55 0 0 1 114 58L59 58Z" fill="var(--gauge-green)"/>
        <path d="M4 58A55 55 0 0 1 114 58" fill="none" stroke="#333" stroke-width="2"/>
        <line x1="59" y1="58" x2="106" y2="42" stroke="#111" stroke-width="3"/>
        <circle cx="59" cy="58" r="5" fill="#111"/><circle cx="59" cy="58" r="2" fill="#fff"/>
      </svg>
      <div class="ends"><span>Needs Attention</span><span>Verified</span></div>
      <span class="pill">Rental Address Verification</span>
    </div>
    <div class="gauge">
      <svg width="118" height="62" viewBox="0 0 118 62">
        <path d="M4 58A55 55 0 0 1 31 11L59 58Z" fill="var(--gauge-red)"/>
        <path d="M31 11A55 55 0 0 1 87 11L59 58Z" fill="var(--gauge-orange)"/>
        <path d="M87 11A55 55 0 0 1 114 58L59 58Z" fill="var(--gauge-green)"/>
        <path d="M4 58A55 55 0 0 1 114 58" fill="none" stroke="#333" stroke-width="2"/>
        <line x1="59" y1="58" x2="104" y2="38" stroke="#111" stroke-width="3"/>
        <circle cx="59" cy="58" r="5" fill="#111"/><circle cx="59" cy="58" r="2" fill="#fff"/>
      </svg>
      <div class="ends"><span>Needs Attention</span><span>Verified</span></div>
      <span class="pill">Member Contact Verification</span>
    </div>
    <div class="gauge">
      <svg width="118" height="62" viewBox="0 0 118 62">
        <path d="M4 58A55 55 0 0 1 31 11L59 58Z" fill="var(--gauge-red)"/>
        <path d="M31 11A55 55 0 0 1 87 11L59 58Z" fill="var(--gauge-orange)"/>
        <path d="M87 11A55 55 0 0 1 114 58L59 58Z" fill="var(--gauge-green)"/>
        <path d="M4 58A55 55 0 0 1 114 58" fill="none" stroke="#333" stroke-width="2"/>
        <line x1="59" y1="58" x2="112" y2="57" stroke="#111" stroke-width="3"/>
        <circle cx="59" cy="58" r="5" fill="#111"/><circle cx="59" cy="58" r="2" fill="#fff"/>
      </svg>
      <div class="ends"><span>Needs Attention</span><span>Verified</span></div>
      <span class="pill on">Landlord Contact Information</span>
    </div>
  </div>
</section>

<aside class="box notice">
  <svg width="46" height="46" viewBox="0 0 46 46"><circle cx="23" cy="23" r="22" fill="#d8dde2"/><circle cx="23" cy="23" r="18" fill="#1c6fc4"/><circle cx="24" cy="13" r="3" fill="#fff"/><path d="M20 19h6l-2 15h3v2h-9v-2h2z" fill="#fff"/></svg>
  <span>Some informtion is still required to validate your membership.</span>
</aside>

<div class="rule" style="top:555px"></div>

<h2 class="factors-title" style="font-weight:400">The 5 Factors That Determine Your Credit Score:</h2>
<p class="factors-intro">Your &nbsp;credit score is based on a number of key factors. The most significant is your history of making payments on time</p>

<svg class="pie" width="420" height="320" viewBox="0 0 420 320" role="img" aria-label="Pie chart of the five credit score factors">
  <ellipse cx="232" cy="155" rx="120" ry="96" fill="#000" opacity=".08" transform="translate(6 14)"/>
  <g transform="translate(227 140) scale(1 .8)">
    <g transform="translate(0 18)">
      <path d="M0 0L-20.5-116.2A118 118 0 0 1 106.1 51.7Z" fill="#0629a8"/>
      <path d="M0 0L106.1 51.7A118 118 0 0 1 20.5 116.2Z" fill="#c2650f"/>
      <path d="M0 0L20.5 116.2A118 118 0 0 1-51.7 106.1Z" fill="#b8aa00"/>
      <path d="M0 0L-51.7 106.1A118 118 0 0 1-104.2 55.4Z" fill="#8e0505"/>
      <path d="M0 0L-104.2 55.4A118 118 0 0 1-20.5-116.2Z" fill="#23900a"/>
    </g>
    <path d="M0 0L-20.5-116.2A118 118 0 0 1 106.1 51.7Z" fill="var(--pie-blue)"/>
    <path d="M0 0L106.1 51.7A118 118 0 0 1 20.5 116.2Z" fill="var(--pie-orange)"/>
    <path d="M0 0L20.5 116.2A118 118 0 0 1-51.7 106.1Z" fill="var(--pie-yellow)"/>
    <path d="M0 0L-51.7 106.1A118 118 0 0 1-104.2 55.4Z" fill="var(--pie-red)"/>
    <path d="M0 0L-104.2 55.4A118 118 0 0 1-20.5-116.2Z" fill="var(--pie-green)"/>
  </g>
  <g fill="#fff" font-family="Arimo, Arial, sans-serif" font-size="16" text-anchor="middle">
    <text x="287" y="110">35%</text>
    <text x="272" y="194">15%</text>
    <text x="217" y="210">10%</text>
    <text x="170" y="191">10%</text>
    <text x="160" y="120">30%</text>
  </g>
</svg>
<div class="pie-label" style="left:86px;top:681px">Amount<br>Owned</div>
<div class="pie-label" style="left:388px;top:684px">Payment<br>History</div>
<div class="pie-label" style="left:61px;top:791px">Types Of<br>Credit</div>
<div class="pie-label" style="left:148px;top:877px">New<br>Credit</div>
<div class="pie-label" style="left:278px;top:911px">Credit<br>Histroy</div>

<section class="box legend">
  <h3><i style="background:var(--pie-blue)"></i>Payment History (35%)</h3>
  <p>Prospective creditors put most weight on how &nbsp;you've made your payments in the past and consider that a clear indication of how you will pay back their loan.</p>
  <h3><i style="background:var(--pie-green)"></i>Amount Owned (30%)</h3>
  <p>A close second in importance is the amount you owe. Creditors are cautious not to have their loan be the one that puts you over the top financially.</p>
  <h3><i style="background:var(--pie-orange)"></i>Credit History (15%)</h3>
  <p>Your history of borrowing is important to prospective new lenders. They look to see whether you've used credit wisely in the past - an indication of how you might use it in the future.</p>
  <h3><i style="background:var(--pie-red)"></i>Types Of Credit (10%)</h3>
  <p>The type of credit you use is important. Do you use bank credit lines or payday loans to make it through a month? Is the credit you get difficult or easy to get?</p>
  <h3><i style="background:var(--pie-yellow)"></i>New Credit (10%)</h3>
  <p>The type of credit you use is important. Do you use bank credit lines or payday loans to make it through a month? Is the credit you get difficult or easy to get?</p>
</section>

<div class="box card" style="left:52px">
  <h4>Histroy</h4>
  <div class="icon"><svg width="46" height="46" viewBox="0 0 46 46"><circle cx="18" cy="18" r="12" fill="#d9eefa" stroke="#3a8fd0" stroke-width="3"/><path d="M27 27l13 13" stroke="#e59a1a" stroke-width="6" stroke-linecap="round"/></svg></div>
  <p>Have you ever<br>made late payments?</p>
  <span class="btn">More Info</span>
</div>
<div class="box card" style="left:182px">
  <h4>Balances</h4>
  <div class="icon"><svg width="40" height="50" viewBox="0 0 40 50"><text x="20" y="44" text-anchor="middle" font-family="Arimo, Arial, sans-serif" font-size="48" font-weight="700" fill="#1ba8d6">$</text></svg></div>
  <p>Do you have<br>high balances?</p>
  <span class="btn">More Info</span>
</div>
<div class="box card" style="left:313px">
  <h4>Acct. Age</h4>
  <div class="icon"><svg width="48" height="50" viewBox="0 0 48 50"><rect x="4" y="22" width="11" height="26" fill="#f2d95a"/><rect x="17" y="10" width="11" height="38" fill="#8fd35b"/><rect x="30" y="2" width="11" height="46" fill="#3d8fe0"/></svg></div>
  <p>How old are your credit<br>accounts?</p>
  <span class="btn">More Info</span>
</div>
<div class="box card" style="left:445px">
  <h4>New Credit</h4>
  <div class="icon"><svg width="54" height="52" viewBox="0 0 54 52"><path d="M27 2l7 17h18l-15 11 6 19-16-11-16 11 6-19L2 19h18z" fill="#2fa6e0" stroke="#0d5f9e" stroke-width="1.5"/></svg></div>
  <p>Have you opened a<br>new account lately ?</p>
  <span class="btn">More Info</span>
</div>
<div class="box card" style="left:575px">
  <h4>Types</h4>
  <div class="icon"><svg width="58" height="40" viewBox="0 0 58 40"><rect x="1" y="2" width="56" height="36" rx="3" fill="#d9dde2" stroke="#9aa1a8"/><rect x="6" y="7" width="46" height="26" rx="2" fill="none" stroke="#9aa1a8"/><text x="29" y="29" text-anchor="middle" font-family="Arimo, Arial, sans-serif" font-size="22" font-weight="700" fill="#8a9299">$</text></svg></div>
  <p>What type of account<br>do you have?</p>
  <span class="btn">More Info</span>
</div>

<div class="cta">
  <div class="big">Continue<br>to your<br>Rent profile</div>
  <div class="more"><svg width="30" height="16" viewBox="0 0 30 16"><path d="M1 1l7 7-7 7h6l7-7-7-7zM14 1l7 7-7 7h6l7-7-7-7z" fill="#fff"/></svg>Read More</div>
</div>

<div class="rule" style="top:1168px"></div>
<div class="copyright">Copyright © 2012 Logo Goes Here.</div>

</body>
</html>
```